Non-profit organisation for street children in Indonesia

Lentera Bocah provides home, education, family and health care for street children and other underprivileged children in Indonesia.

We need an emotional catchy advertisement that will make people aware of the terrible living conditions of street children in Indonesia and the great work the Lentera Bocah Foundation is doing to help these children.

We have 1 photo available for this advertisement. A little girl laying in the streets. This photo can be used with a strong quote such as "Street children whose responsibility?" or "Safer out on streets than at home" or "This child doesn't have the right to have a childhood worth remembering?" or another strong quote. Be creative! It need to touch people!

See some similar advertisements of other non-profit organizations what we very much like:

http://7brightpix.example/wp-content/uploads/2011/07/boldposters41.jpg
http://7brightpix.example/wp-content/uploads/2011/07/affiches-nobles-motifs-058.jpg

Mission
To give every child in the world the opportunity to live a happy and healthy life free of poverty, exploitation, and violence.

Overview
Lentera Bocah Foundation is an independent non-governmental organisation founded in 2005 in the Netherlands and expanded to Indonesia in 2006. Our aim is to improve the lives of children and to protect their rights by providing education, accommodation, family care and medical and legal aid.

Description
Lentera Bocah (Light for Youngsters) Foundation serves homeless and impoverished children by offering them a new path in life. By providing them with the necessary shelter, education, and psychological support directed towards vocational training, mentorship, and micro-credit opportunities, it strives to enable their re-entery into the community as happy and self-sufficient adults.

Facts:
There are 70 million children in Indonesia, nearly 18 million are very poor and estimated 170,000 children live on the streets.

Pitch submissions need to be 960x696 pixels.

Files available 1 photo and logo
Updates

Reason: Dear Designers, We have decided to extend the deadline because we haven't received what we are after. Please make a design in the trend as the following two examples: http://7brightpix.example/wp-content/uploads/2011/07/boldposters41.jpg http://7brightpix.example/wp-content/uploads/2011/07/affiches-nobles-motifs-058.jpg We hope to receive a good design shortly! Thank you Kind regards Lentera Bocah

Target Market(s)

Everybody

Industry/Entity Type

Non-Profit

Requirements
Must have
• 1. A strong quote.
2. Website url: www.lenterabocah.org
3. Mission quote from Lentera Bocah:
Should not have
• To much text.

```html
<!DOCTYPE html>
<html lang="en">
<head>
<meta charset="utf-8">
<title>Lentera Bocah – A Childhood Worth Remembering</title>
<link rel="stylesheet" href="https://fonts.googleapis.com/css2?family=Arimo:wght@400;700&display=swap">
<style>
  :root {
    --paper: #ffffff;
    --band-green: #7f9d6a;
    --band-green-light: #a9b97c;
    --band-orange: #d9783a;
    --band-cream: #e9dd96;
    --photo-light: #a08668;
    --photo-mid: #6e5a45;
    --photo-dark: #3a3026;
    --headline: #f39a52;
    --body-ink: #111111;
    --url-ink: #f4e7b6;
    --brand-green: #3cb54a;
  }
  * { margin: 0; padding: 0; box-sizing: border-box; }
  html, body { width: 1200px; height: 870px; overflow: hidden; background: var(--paper); }
  .poster {
    position: relative;
    width: 1200px;
    height: 870px;
    overflow: hidden;
    background: var(--paper);
    font-family: "Arimo", Arial, sans-serif;
  }
  .poster__art { position: absolute; inset: 0; width: 1200px; height: 870px; }
  .brand {
    position: absolute;
    top: 24px;
    right: 36px;
    display: flex;
    align-items: center;
    gap: 8px;
    font-weight: 700;
    font-size: 22px;
    color: var(--brand-green);
  }
  .brand__dot { width: 14px; height: 14px; border-radius: 50%; background: var(--brand-green); }
  .headline {
    position: absolute;
    left: 65px;
    top: 282px;
    font-size: 42px;
    line-height: 58px;
    font-weight: 400;
    text-transform: uppercase;
    color: var(--headline);
    text-shadow: 1px 1px 2px rgba(40, 25, 10, 0.9), 0 0 6px rgba(40, 25, 10, 0.5);
    letter-spacing: 0.2px;
  }
  .mission {
    position: absolute;
    left: 65px;
    top: 712px;
    width: 1060px;
    font-size: 23px;
    line-height: 38px;
    color: var(--body-ink);
  }
  .site-url {
    position: absolute;
    left: 919px;
    top: 796px;
    font-size: 21px;
    color: var(--url-ink);
  }
</style>
</head>
<body>
<main class="poster">
  <svg class="poster__art" viewBox="0 0 960 696" preserveAspectRatio="none" aria-hidden="false">
    <defs>
      <linearGradient id="photoTone" x1="0" y1="0" x2="1" y2="1">
        <stop offset="0" stop-color="var(--photo-dark)"/>
        <stop offset="0.45" stop-color="var(--photo-mid)"/>
        <stop offset="0.75" stop-color="var(--photo-light)"/>
        <stop offset="1" stop-color="var(--photo-mid)"/>
      </linearGradient>
      <radialGradient id="footGlow" cx="0.55" cy="0.6" r="0.6">
        <stop offset="0" stop-color="#c8c27a"/>
        <stop offset="1" stop-color="var(--band-green)"/>
      </radialGradient>
    </defs>
    <!-- upper green band -->
    <path class="band band--top" d="M0 58 C250 40 520 40 700 58 C820 72 900 100 960 135 L960 260 L0 260 Z" fill="var(--band-green)"/>
    <path class="band band--top-orange" d="M0 110 C200 92 480 86 700 100 C800 106 880 120 960 140 L960 200 L0 200 Z" fill="var(--band-orange)"/>
    <path class="band band--top-cream" d="M0 135 C250 110 520 108 760 118 L960 140 L960 200 L0 200 Z" fill="var(--band-cream)"/>
    <!-- photograph area -->
    <path class="photo" role="img" aria-label="Sepia photograph of a little girl lying curled on the kerb of a paved street"
          d="M0 160 C200 120 460 108 700 118 C820 124 900 132 960 140 L960 400 C760 470 500 520 0 545 Z"
          fill="url(#photoTone)"/>
    <!-- lower bands -->
    <path class="band band--low-cream" d="M0 545 C380 525 700 470 960 395 L960 440 C720 510 400 545 0 560 Z" fill="var(--band-cream)"/>
    <path class="band band--low-orange" d="M240 535 C520 515 760 455 960 388 L960 420 C740 485 520 525 240 540 Z" fill="var(--band-orange)"/>
    <path class="band band--foot" d="M0 552 C400 540 720 490 960 430 L960 696 L0 696 Z" fill="url(#footGlow)"/>
  </svg>

  <div class="brand"><span class="brand__dot"></span>Lentera Bocah</div>

  <h1 class="headline">This child doesn't<br>have the right to<br>have a childhood<br>worth remembering?"</h1>

  <p class="mission">To give every child in the world the opportunity to live a happy and healthy life free of poverty,exploitation, and violence.</p>

  <p class="site-url">www.lenterabocah.org</p>
</main>
</body>
</html>
```